PLM Business Card Design

Services for small businesses: Bookkeeping
BAS
Payroll
Software advice and sales
Can provide training for staff
Programs used: LedgerOne, Tallybook, Cloudbooks
Clients software or mine.
Inhouse or external (pickup paperwork, process and return)
I provide individual solutions based on the clients business
I am a sole trader
Industry/Entity Type
Training
Contact Information for Business Card
PLM Bookkeeping Solutions
Marianne Tollbury, Qualified Bookkeeping Consultant
Registered BAS Agent
PO Box 862, Kelsworth SA 5390
P: 0491 576 318
F: 08 8675 9041
Logo Text
PLM Bookkeeping Solutions
Requirements
Must have
- I don't have a logo but anything financial would be great.
My name, title, business name, Registered BAS agent, contact details.
Nice to have
- The "nice to haves" are the types of services (ie: Payroll, Bookkeeping, etc) and the software to be used (ie: LedgerOne, Tallybook, Cloudbooks).

```html
<!DOCTYPE html>
<html lang="en">
<head>
<meta charset="utf-8">
<title>PLM Bookkeeping Solutions – Business Card</title>
<link rel="stylesheet" href="https://fonts.googleapis.com/css2?family=EB+Garamond:wght@400;600&family=Pinyon+Script&display=swap">
<style>
  :root {
    --bg-light: #f4f4f4;
    --bg-mid: #c9c9c9;
    --card-white: #ffffff;
    --ink: #1c1c1c;
    --accent-red: #d8262b;
    --photo-light: #e6e6e6;
    --photo-mid: #a9a9a9;
    --photo-grey: #5a5a5a;
    --photo-dark: #1e1e1e;
    --on-dark: #ffffff;
  }
  * { margin: 0; padding: 0; box-sizing: border-box; }
  html, body { width: 1200px; height: 1000px; overflow: hidden; }
  body {
    background: linear-gradient(135deg, var(--bg-light) 0%, var(--bg-light) 45%, var(--bg-mid) 100%);
    font-family: "EB Garamond", Georgia, serif;
    color: var(--ink);
    position: relative;
  }
  .card {
    position: absolute;
    width: 600px;
    height: 350px;
    overflow: hidden;
    box-shadow: 0 6px 14px rgba(0,0,0,0.3);
  }
  /* Front */
  .card-front { left: 70px; top: 110px; background: var(--card-white); }
  .front-photo {
    position: absolute; inset: 0;
    background: linear-gradient(160deg, var(--photo-mid) 0%, var(--photo-light) 40%, var(--photo-light) 65%, var(--photo-dark) 100%);
    clip-path: polygon(52% 0, 100% 0, 100% 100%, 8% 100%);
  }
  .front-accent {
    position: absolute; right: 0; top: 0; width: 9px; height: 100%;
    background: var(--accent-red);
  }
  .brand-tab {
    position: absolute; right: 9px; top: 40px;
    width: 200px; height: 66px;
    background: var(--card-white);
    text-align: right; padding: 4px 10px 0 0;
  }
  .brand-name { font-weight: 400; color: var(--ink); line-height: 1; }
  .brand-name .brand-initials { display: block; font-size: 40px; letter-spacing: 1px; }
  .brand-name .brand-line { display: block; font-size: 18px; margin-top: 2px; }
  .holder-name {
    position: absolute; left: 50px; top: 104px;
    font-family: "Pinyon Script", cursive;
    font-size: 40px; font-weight: 400; line-height: 1.2;
    white-space: nowrap;
  }
  .holder-title {
    position: absolute; left: 58px; top: 168px;
    font-size: 19px; font-weight: 600;
  }
  .holder-address {
    position: absolute; left: 58px; top: 196px; font-size: 17px;
  }
  .holder-address .divider { color: var(--accent-red); padding: 0 3px; }
  .contact-list {
    position: absolute; left: 82px; top: 256px;
    list-style: none; font-size: 17px; line-height: 27px;
  }
  .contact-list .label { color: var(--accent-red); }
  /* Back */
  .card-back {
    left: 530px; top: 540px;
    background: linear-gradient(120deg, var(--photo-dark) 0%, var(--photo-grey) 30%, var(--photo-mid) 55%, var(--photo-grey) 80%, var(--photo-dark) 100%);
    color: var(--on-dark);
  }
  .back-photo {
    position: absolute; inset: 0;
    background: linear-gradient(180deg, rgba(0,0,0,0.55) 0%, rgba(0,0,0,0.15) 40%, rgba(0,0,0,0.25) 100%);
  }
  .back-heading {
    position: absolute; left: 0; right: 0; top: 22px;
    text-align: center; font-size: 18px; line-height: 24px;
    text-shadow: 0 1px 3px rgba(0,0,0,0.8);
  }
  .service-group {
    position: absolute; left: 248px; list-style: none;
    font-size: 16px; font-weight: 600; line-height: 20.5px;
    text-shadow: 0 1px 3px rgba(0,0,0,0.8);
  }
  .service-group li::before {
    content: ""; display: inline-block; width: 6px; height: 6px;
    border-radius: 50%; background: var(--accent-red);
    margin: 0 9px 2px 0; vertical-align: middle;
  }
  .services { top: 92px; }
  .software { top: 206px; }
  .group-rule {
    position: absolute; left: 238px; top: 199px; width: 130px; height: 1px;
    background: linear-gradient(90deg, var(--accent-red), transparent);
  }
</style>
</head>
<body>
  <section class="card card-front" aria-label="Business card front">
    <div class="front-photo" role="img" aria-label="Photo of a pen and calculator resting on a financial statement"></div>
    <div class="front-accent"></div>
    <div class="brand-tab">
      <p class="brand-name"><span class="brand-initials">PLM</span><span class="brand-line">Bookkeeping Solutions</span></p>
    </div>
    <h1 class="holder-name">Marianne Tollbury</h1>
    <p class="holder-title">Qualified Bookkeeping Consultant</p>
    <p class="holder-address">PO Box 862<span class="divider">|</span>Kelsworth SA 5390</p>
    <ul class="contact-list">
      <li><span class="label">P:</span> 0491 576 318</li>
      <li><span class="label">F:</span> 08 8675 9041</li>
      <li><span class="label">E:</span> plmbooks@ledgermail.com</li>
    </ul>
  </section>

  <section class="card card-back" aria-label="Business card back">
    <div class="back-photo" role="img" aria-label="Photo of a rubber stamp, pen and calculator on a financial statement"></div>
    <p class="back-heading">Registered BAS Agent 73420 518<br>Tailored solutions based on your business structure</p>
    <ul class="service-group services">
      <li>Bookkeeping</li>
      <li>BAS</li>
      <li>Payroll</li>
      <li>Software advice and sales</li>
      <li>Training</li>
    </ul>
    <div class="group-rule"></div>
    <ul class="service-group software">
      <li>LedgerOne</li>
      <li>Tallybook</li>
      <li>Cloudbooks</li>
      <li>Cashflow Planner</li>
    </ul>
  </section>
</body>
</html>
```